Weaving Tales Past Screens

We are running an international event in Switzerland on "Transmedia" with some of the hottest names in this hot media space ...

There will be 15 Keynote addresses and we are paying to have them professionally transcribed, copywritten, and proof-read to be published in an eBook.

The 15 Keynotes reference a huge number of global media brands - have a look: www.quorvanthub.com

We want a riveting, beautifully designed eBook cover and layout strategy - with the idea that this will be first of a series we will publish on different "Creative Industries" professional development issues - so MOST important is to think of the ARCHITECTURE of the artwork, as well as the graphic design ... think of the idea of an "imprint" in traditional book publishing - the architecture will remain the same, but the artwork and imagry will change each time.

Core values: Global media, Excellence, World's Best practitioners, Know How-to, Instant Inside Knowledge.

Target Market(s)

Professional Development for International Creative Industries Practitioners.

Industry/Entity Type

Graphic Design

Requirements
Must have
• Should be re-purposable across all other forms of media: it's "Transmedia", right? It should incorporate artwork, design, operate as a logo, typeface and font, and a basic imprint for a series of eBooks

The most important consideration in buying an Book is the Table of Content and the authors (we've got that in gold!) - The second-most important consideration is the artwork on the cover ... it has to be instantly convincing.

```html
<!DOCTYPE html>
<html lang="en">
<head>
<meta charset="utf-8">
<title>Weaving Tales Past Screens — eBook Cover</title>
<link rel="stylesheet" href="https://fonts.googleapis.com/css2?family=Bebas+Neue&display=swap">
<style>
  :root {
    --page: #ffffff;
    --cover-light: #ffffff;
    --cover-shade: #ececec;
    --signal-red: #ee2b24;
    --signal-red-warm: #f0402a;
    --amber: #f9a51b;
    --sky: #00bdf2;
    --sky-pale: #bfe8fa;
    --ghost: #e4e4e4;
    --ink-light: #ffffff;
  }
  * { margin: 0; padding: 0; box-sizing: border-box; }
  html, body {
    width: 1200px;
    height: 900px;
    overflow: hidden;
    background: var(--page);
  }
  .canvas {
    position: relative;
    width: 1200px;
    height: 900px;
    overflow: hidden;
  }
  .cover {
    position: absolute;
    left: 330px;
    top: 43px;
    width: 542px;
    height: 814px;
    overflow: hidden;
    background: radial-gradient(ellipse at 55% 55%, var(--cover-light) 35%, var(--cover-shade) 100%);
  }
  .cover > * { position: absolute; }

  .title-pill {
    left: 0;
    top: 7px;
    width: 335px;
    height: 320px;
    border-radius: 0 160px 160px 0;
    background: linear-gradient(90deg, var(--signal-red-warm), var(--signal-red));
    display: flex;
    align-items: center;
    justify-content: center;
    padding-right: 10px;
  }
  .title {
    font-family: "Bebas Neue", "Oswald", sans-serif;
    font-weight: 400;
    font-size: 54px;
    line-height: 1.32;
    letter-spacing: 2px;
    color: var(--ink-light);
    text-align: center;
    text-transform: uppercase;
  }

  .drip-bar { top: 0; border-radius: 0 0 20px 20px; }
  .drip-bar--amber { left: 353px; width: 35px; height: 249px; background: var(--amber); }
  .drip-bar--sky   { left: 411px; width: 29px; height: 194px; background: var(--sky); }
  .drip-bar--red   { left: 456px; width: 45px; height: 354px; background: var(--signal-red); }

  .ghost-bar { background: var(--ghost); border-radius: 0 0 10px 10px; opacity: 0.7; }
  .ghost-bar--one   { left: 20px; top: 327px; width: 18px; height: 120px; }
  .ghost-bar--two   { left: 48px; top: 327px; width: 17px; height: 30px; }
  .ghost-bar--three { left: 80px; top: 327px; width: 18px; height: 62px; }

  .monogram-art {
    left: 115px;
    top: 357px;
    width: 350px;
    height: 255px;
    border-radius: 40% 45% 40% 50%;
    background: radial-gradient(ellipse at 50% 50%, var(--sky) 0%, var(--sky-pale) 55%, rgba(191,232,250,0) 75%);
  }

  .pixel { width: 48px; height: 48px; }
  .pixel--amber { background: var(--amber); }
  .pixel--sky   { background: var(--sky); }
  .pixel--red   { background: var(--signal-red); }

  .badge-pill {
    left: 327px;
    top: 665px;
    width: 215px;
    height: 140px;
    border-radius: 70px 0 0 70px;
    background: linear-gradient(90deg, var(--signal-red-warm), var(--signal-red));
  }
  .badge-cross {
    left: 349px;
    top: 714px;
    width: 42px;
    height: 42px;
  }
  .badge-cross::before,
  .badge-cross::after {
    content: "";
    position: absolute;
    background: var(--ink-light);
  }
  .badge-cross::before { left: 14px; top: 0; width: 14px; height: 42px; }
  .badge-cross::after  { left: 0; top: 14px; width: 42px; height: 14px; }
</style>
</head>
<body>
<main class="canvas">
  <section class="cover">
    <div class="ghost-bar ghost-bar--one"></div>
    <div class="ghost-bar ghost-bar--two"></div>
    <div class="ghost-bar ghost-bar--three"></div>

    <div class="title-pill">
      <h1 class="title">Weaving Tales<br>Past Screens</h1>
    </div>

    <div class="drip-bar drip-bar--amber"></div>
    <div class="drip-bar drip-bar--sky"></div>
    <div class="drip-bar drip-bar--red"></div>

    <div class="monogram-art" role="img" aria-label="Sky-blue ribbon letter A illustration with a dripping edge"></div>

    <div class="pixel pixel--amber" style="left:0;top:570px"></div>
    <div class="pixel pixel--amber" style="left:145px;top:619px"></div>
    <div class="pixel pixel--sky" style="left:0;top:667px"></div>
    <div class="pixel pixel--red" style="left:97px;top:667px"></div>
    <div class="pixel pixel--red" style="left:193px;top:667px"></div>
    <div class="pixel pixel--amber" style="left:48px;top:715px"></div>
    <div class="pixel pixel--sky" style="left:0;top:763px"></div>
    <div class="pixel pixel--red" style="left:97px;top:763px"></div>

    <div class="badge-pill"></div>
    <div class="badge-cross" aria-hidden="true"></div>
  </section>
</main>
</body>
</html>
```